Clean book cover design for book about writing a book

Book title: The Turning
Subtitle: 10 Paths to Crafting a Volume of Weight
Name: Mirela K. Dunwoody, The Quill Nestery

This is a book which teaches 10 steps to writing a self-help book. I'm looking for a very clean impactful cover either with no image or just a small simple image of a book, typewriter, laptop, cabin or something very simple. I am attaching the manuscript here if reading it would help you with the cover. The theme of the book is that you can write with joy and ease and your book can just flow out of you if you learn how to clear the blocks between you and your book already written. Sort of a new agey stance on book writing.

The book should generally match the branding on my website. Www.TheQuillNestery.example.

I have photos of myself attached which I'd like used for the back cover with an "about the author section of maybe 50 words.

The project is for the full back cover and spine as well as the front cover (see press Forge template attached) but to win the contest you can just design the front cover and then I'll give the winner the template for the full design with the back cover copy. Or you can design the full cover using the template and you can use Loren ipsum text if you need to.

My clients are very upmarket and the themes of my business revolve around nuturing and incubating ideas and authors. Very feminine creation energy.

For colors see The Turning Press (TH) wax seals and the background fades. I don't want my logo on the cover but I am attaching it here so you get a feel for the branding. The logo is in the LOBSTER font and you can see how we do the grey with the rainbow shadow.

Here are some covers I like:

http://www.bookmarto.example/Pen-Volume-Fast-Stage---Stage/dp/071302488Q
http://www.bookmarto.example/Sketching-Their-Tale-Chart-Triumph/dp/0865713511
http://www.bookmarto.example/Be-Scribe-Seeking-Poet-Guide-ebook/dp/C11G8V9PL7
http://www.bookmarto.example/Strayfolk-Tale-Triumph-Rupert-Hallowmere/dp/0427128041
Updates

I have revised my brief to include some picture and images that will help you create the cover. I have also included some of my favorite covers to give you more of a sense of what I'm going for. And I have included the manuscript in case it would help you to skim through it in order to get a sense of the reader and the book. I think if you look at my revised brief it will make it easier to create a submission. Thanks!

Target Market(s)

Women 40-60 who run small businesses as life coaches or other healing jobs (therapy, reiki, light work) they have a spiritual/new age bent.

Industry/Entity Type

Business

Font styles to use
Serif
Other font styles liked:
• Lobster (not required... just a suggestion since it's my logo font)

Requirements
Must have
• Name and title easy to read in 1" x 1" thumb nail
Nice to have
• Fantastic type face treatment.

Match the look and feel of my website.
Should not have
• Busy images. With one simple image or just designed with colors and typeface treatment

```html
<!DOCTYPE html>
<html lang="en">
<head>
<meta charset="utf-8">
<title>The Turning — Book Cover Spread</title>
<link rel="stylesheet" href="https://fonts.googleapis.com/css2?family=Lobster&family=Jost:wght@400;500;600;700&display=swap">
<style>
  :root {
    --canvas: #f1f1f0;
    --paper: #e7e3dd;
    --paper-edge: #d9d4cd;
    --ink: #141414;
    --art-warm: #e6c64a;
    --art-soft: #e2b3b6;
    --seal: #3d4f9e;
    --photo-dark: #2e3a34;
    --photo-light: #d9c48a;
    --white: #ffffff;
  }
  * { box-sizing: border-box; margin: 0; padding: 0; }
  html, body { width: 1200px; height: 800px; overflow: hidden; }
  body {
    background: var(--canvas);
    font-family: "Jost", "Century Gothic", sans-serif;
    color: var(--ink);
  }
  .cover-spread {
    position: absolute;
    left: 208px;
    top: 115px;
    display: flex;
    height: 570px;
    box-shadow: 0 18px 40px rgba(0,0,0,.12);
  }
  .panel {
    position: relative;
    height: 100%;
    background: radial-gradient(ellipse at 50% 40%, #ece9e4 0%, var(--paper) 60%, var(--paper-edge) 100%);
  }
  /* ---------- back cover ---------- */
  .back-cover { width: 370px; padding: 26px 20px 0; }
  .back-title {
    font-family: "Lobster", cursive;
    font-size: 44px;
    font-weight: 400;
    text-align: center;
    line-height: 1;
  }
  .back-subtitle {
    font-size: 15px;
    font-weight: 600;
    text-align: center;
    margin-top: 4px;
  }
  .back-copy {
    font-size: 9.4px;
    font-weight: 700;
    line-height: 1.2;
    text-align: justify;
    margin-top: 8px;
  }
  .about-author {
    display: flex;
    gap: 12px;
    margin-top: 12px;
    align-items: flex-start;
  }
  .about-author .back-copy { margin-top: 0; flex: 1; }
  .author-photo {
    width: 92px;
    height: 98px;
    flex: none;
    background: radial-gradient(circle at 50% 38%, var(--photo-light) 0%, #b99e6a 35%, var(--photo-dark) 75%);
  }
  .publisher-mark {
    position: absolute;
    left: 20px;
    bottom: 22px;
    display: flex;
    align-items: center;
    gap: 6px;
  }
  .publisher-mark .dot {
    width: 46px; height: 46px;
    border-radius: 50%;
    background: var(--seal);
  }
  .publisher-mark .name {
    font-size: 13px;
    font-weight: 600;
    color: var(--seal);
  }
  .isbn-box {
    position: absolute;
    right: 24px;
    bottom: 22px;
    width: 94px;
    height: 44px;
    background: var(--white);
    display: flex;
    align-items: center;
    justify-content: center;
    font-size: 17px;
    font-weight: 700;
  }
  /* ---------- spine ---------- */
  .spine {
    width: 44px;
    border-left: 1px solid var(--paper-edge);
    border-right: 1px solid var(--paper-edge);
    display: flex;
    flex-direction: column;
    align-items: center;
    padding-top: 22px;
    gap: 40px;
  }
  .spine-title, .spine-author { writing-mode: vertical-rl; white-space: nowrap; }
  .spine-title { font-family: "Lobster", cursive; font-size: 30px; line-height: 1; }
  .spine-author { font-size: 10px; font-weight: 600; letter-spacing: .5px; }
  /* ---------- front cover ---------- */
  .front-cover { width: 370px; overflow: hidden; }
  .front-title { font-family: "Lobster", cursive; font-weight: 400; line-height: 1; }
  .front-title .word { position: absolute; white-space: nowrap; }
  .front-title .word-the { left: 70px; top: 165px; font-size: 62px; transform: rotate(-18deg); }
  .front-title .word-main { left: 22px; top: 240px; font-size: 86px; transform: rotate(-24deg); transform-origin: left center; }
  .cover-art {
    position: absolute;
    left: 290px;
    top: 36px;
    width: 62px;
    height: 130px;
    background: linear-gradient(to bottom, var(--art-soft) 0%, var(--art-warm) 55%, rgba(230,198,74,.35) 100%);
    border-radius: 6px;
  }
  .front-subtitle {
    position: absolute;
    right: 30px;
    top: 350px;
    text-align: right;
    font-size: 22px;
    font-weight: 600;
    line-height: 1.3;
  }
  .front-author {
    position: absolute;
    left: 0; right: 0;
    top: 500px;
    text-align: center;
  }
  .front-author .name { font-size: 15px; font-weight: 700; }
  .front-author .imprint { font-size: 12px; font-weight: 600; margin-top: 2px; }
</style>
</head>
<body>
<main class="cover-spread">
  <section class="panel back-cover">
    <h2 class="back-title">The Turning</h2>
    <p class="back-subtitle">10 Paths to Crafting a Volume of Weight</p>
    <p class="back-copy">Lorem ipsum dolor sit amet, consectetur adipisicing elit, sed do eiusmod tempor incididunt ut labore et dolore magna aliqua. Ut enim ad minim veniam, quis nostrud exercitation. Lorem ipsum dolor sit amet, consectetur adipisicing elit, sed do eiusmod tempor incididunt ut labore et dolore magna aliqua. Ut enim ad minim veniam, quis nostrud exercitation. Lorem ipsum dolor sit amet, consectetur adipisicing elit, sed do eiusmod tempor incididunt ut labore et dolore magna aliqua. Ut enim ad minim veniam, quis nostrud exercitation. Lorem ipsum dolor sit amet, consectetur adipisicing elit, sed do eiusmod tempor incididunt ut labore et dolore magna aliqua. Ut enim ad minim veniam, quis nostrud exercitation. Lorem ipsum dolor sit amet, consectetur adipisicing elit, sed do eiusmod tempor incididunt ut labore et dolore magna aliqua. Ut enim ad minim veniam, quis nostrud exercitation. Lorem ipsum dolor sit amet, consectetur adipisicing elit, sed do eiusmod tempor incididunt ut labore et dolore magna aliqua. Ut enim ad minim veniam, quis nostrud exercitation. Lorem ipsum dolor sit amet, consectetur adipisicing elit, sed do eiusmod tempor incididunt ut labore et dolore magna aliqua. Ut enim ad minim veniam, quis nostrud exercitation. Lorem ipsum dolor sit amet, consectetur adipisicing elit, sed do eiusmod tempor incididunt ut labore et dolore magna aliqua.</p>
    <div class="about-author">
      <p class="back-copy">Lorem ipsum dolor sit amet, consectetur adipisicing elit, sed do eiusmod tempor incididunt ut labore et dolore magna aliqua. Ut enim ad minim veniam, quis nostrud exercitation. Lorem ipsum dolor sit amet, consectetur adipisicing elit, sed do eiusmod tempor incididunt ut labore et dolore magna aliqua. Ut enim ad minim veniam, quis nostrud exercitation.</p>
      <div class="author-photo" role="img" aria-label="Portrait photograph of the author"></div>
    </div>
    <div class="publisher-mark">
      <span class="dot"></span>
      <span class="name">TH</span>
    </div>
    <div class="isbn-box">ISBN</div>
  </section>

  <section class="panel spine">
    <span class="spine-title">The Turning</span>
    <span class="spine-author">Mirela K. Dunwoody</span>
  </section>

  <section class="panel front-cover">
    <h1 class="front-title">
      <span class="word word-the">The</span>
      <span class="word word-main">Turning</span>
    </h1>
    <div class="cover-art" role="img" aria-label="Illustration of a yellow pencil with a pink eraser, writing the title"></div>
    <p class="front-subtitle">10 Paths to<br>Crafting a Volume<br>of Weight!</p>
    <div class="front-author">
      <p class="name">Mirela K. Dunwoody</p>
      <p class="imprint">The Quill Nestery</p>
    </div>
  </section>
</main>
</body>
</html>
```